Valdora Business Card Design - Professional Flexible and forward thinking. Clean and Easy to follow

Management Consulting Company. I focus on business development and concept and operational review. I need a progressive, simple and professional layout design for the business cards, letterhead and envelops
Professional Flexible and forward thinking. Clean and Easy to follow
Mature Business persons and professionals and Corporations

Target Market(s)

Mature Business persons and professionals and Corporations - Government org.

Industry/Entity Type

Consulting

Contact Information for Business Card

Requirements
Must have
• Marcus Valdora
• President
• Phone - 555.382.6047
• email - Mvaldora@valdorapartners.com
• Skype - Marc.valdora
• 7215 Pellham Avenue
• Suite 4
• Carrow Point, N.Y. 10990
• USA
Nice to have
• www.valdorapartners.com
Should not have
• N/A

```html
<!DOCTYPE html>
<html lang="en">
<head>
<meta charset="utf-8">
<title>Valdora Associates – Business Card</title>
<link rel="stylesheet" href="https://fonts.googleapis.com/css2?family=Montserrat:wght@300;400;600&family=Lato:wght@400;700;900&display=swap">
<style>
  :root {
    --stage: #2b2b2b;
    --paper: #ffffff;
    --paper-edge: #e9e9e9;
    --brand-blue: #1f4f8a;
    --brand-blue-dark: #163c6b;
    --ink: #1d1d1d;
    --muted: #8a8a8a;
    --rule: #9a9a9a;
  }
  * { margin: 0; padding: 0; box-sizing: border-box; }
  html, body { width: 1200px; height: 873px; overflow: hidden; }
  body {
    background: var(--stage);
    position: relative;
    font-family: "Lato", sans-serif;
  }
  .card {
    position: absolute;
    left: 290px;
    width: 620px;
    height: 354px;
    background: linear-gradient(160deg, var(--paper) 0%, var(--paper) 60%, var(--paper-edge) 100%);
    overflow: hidden;
  }
  .card--front { top: 52px; }
  .card--contact { top: 467px; }

  .corner-band {
    position: absolute;
    left: 0; bottom: 0;
    width: 620px; height: 354px;
  }

  .wordmark {
    position: absolute;
    display: flex;
    align-items: center;
    gap: 14px;
  }
  .wordmark__square {
    width: 18px; height: 18px;
    background: var(--brand-blue);
  }
  .wordmark__rule {
    width: 1.5px;
    background: var(--rule);
    align-self: stretch;
  }
  .wordmark__name {
    font-family: "Montserrat", sans-serif;
    font-weight: 600;
    color: var(--brand-blue);
    letter-spacing: 0.5px;
    line-height: 1;
  }
  .wordmark__tagline {
    font-family: "Montserrat", sans-serif;
    font-weight: 300;
    color: var(--muted);
    letter-spacing: 2px;
    line-height: 1;
    margin-top: 5px;
  }
  .card--front .wordmark { left: 130px; top: 140px; }
  .card--front .wordmark__square { width: 26px; height: 26px; }
  .card--front .wordmark__name { font-size: 28px; }
  .card--front .wordmark__tagline { font-size: 18px; }

  .card--contact .wordmark { left: 160px; top: 40px; }
  .card--contact .wordmark__name { font-size: 21px; }
  .card--contact .wordmark__tagline { font-size: 13px; }

  .website {
    position: absolute;
    left: 42px; bottom: 22px;
    font-weight: 900;
    font-size: 13px;
    letter-spacing: 2.5px;
    color: var(--brand-blue);
  }

  .person {
    position: absolute;
    left: 78px; top: 170px;
    text-align: right;
  }
  .person__name {
    font-weight: 900;
    font-size: 22px;
    color: var(--brand-blue);
  }
  .person__title {
    font-size: 14px;
    color: var(--ink);
    margin-top: 2px;
  }
  .divider {
    position: absolute;
    left: 288px; top: 128px;
    width: 3px; height: 120px;
    background: linear-gradient(to bottom, rgba(31,79,138,0) 0%, var(--brand-blue) 50%, rgba(31,79,138,0) 100%);
  }
  .contact-list {
    position: absolute;
    left: 318px; top: 130px;
    list-style: none;
  }
  .contact-list li {
    display: flex;
    align-items: center;
    gap: 10px;
    font-size: 15px;
    color: var(--ink);
    height: 30px;
  }
  .contact-list svg { width: 16px; height: 16px; flex: none; }
  .address {
    position: absolute;
    left: 40px; bottom: 22px;
    font-weight: 900;
    font-size: 16px;
    color: var(--brand-blue);
    white-space: nowrap;
  }
</style>
</head>
<body>

<section class="card card--front" aria-label="Card front">
  <svg class="corner-band" viewBox="0 0 620 354" aria-hidden="true">
    <path d="M372 354 Q372 336 394 336 L620 336 L620 354 Z" fill="var(--brand-blue)"/>
  </svg>
  <div class="wordmark">
    <span class="wordmark__square"></span>
    <span class="wordmark__rule"></span>
    <div>
      <div class="wordmark__name">VALDORA ASSOCIATES</div>
      <div class="wordmark__tagline">Management Consulting</div>
    </div>
  </div>
  <p class="website">www.valdorapartners.com</p>
</section>

<section class="card card--contact" aria-label="Card back">
  <svg class="corner-band" viewBox="0 0 620 354" aria-hidden="true">
    <path d="M372 354 Q372 336 394 336 L620 336 L620 354 Z" fill="var(--brand-blue)"/>
  </svg>
  <div class="wordmark">
    <span class="wordmark__square"></span>
    <span class="wordmark__rule"></span>
    <div>
      <div class="wordmark__name">VALDORA ASSOCIATES</div>
      <div class="wordmark__tagline">Management Consulting</div>
    </div>
  </div>

  <div class="person">
    <div class="person__name">Marcus Valdora</div>
    <div class="person__title">President</div>
  </div>

  <span class="divider"></span>

  <ul class="contact-list">
    <li>
      <svg viewBox="0 0 16 16" aria-hidden="true"><path d="M1 6 Q8 1 15 6 L13 8 L11 6 L5 6 L3 8 Z M4 9 L12 9 L14 14 L2 14 Z" fill="var(--brand-blue-dark)"/></svg>
      555.382.6047
    </li>
    <li>
      <svg viewBox="0 0 16 16" aria-hidden="true"><rect x="1" y="3" width="14" height="10" fill="var(--brand-blue-dark)"/><path d="M1 3 L8 9 L15 3" fill="none" stroke="#fff" stroke-width="1.3"/></svg>
      Mvaldora@valdorapartners.com
    </li>
    <li>
      <svg viewBox="0 0 16 16" aria-hidden="true"><circle cx="8" cy="8" r="7" fill="var(--brand-blue-dark)"/></svg>
      Marc.valdora
    </li>
  </ul>

  <p class="address">7215 Pellham Avenue, Suite 4, Carrow Point, N.Y. 10990, USA</p>
</section>

</body>
</html>
```